Computer consultant business card

Brimlo Software is a newly started computer consulting company. It's a small one-man company that provides mostly Velunix applications but also websites in collaboration with designers. I'm running this company on the side of full time university studies.

I want the final design to be clean and memorable. Be creative! :)

Some inspiration:
http://www.tavelpix.net/design/73519
http://www.tavelpix.net/design/2739566/business-card-design-by-quillbop
http://www.tavelpix.net/design/804613/business-card-design-by-lorvena-brukwaldsen

See attachment for my company logo.
Updates

I would like to thank everyone for submitting! I'll need a couple of days to review and ultimately select a design.

Target Market(s)

Non-technical entrepreneurs and small companies.

Industry/Entity Type

University

Requirements
Must have
• My company logo.
In any way, both colors from my logo.
First- and last name, e-mail and phone number.
Double-sided design.
Nice to have
• Something creative with the symbol in my logo

```html
<!DOCTYPE html>
<html lang="en">
<head>
<meta charset="utf-8">
<title>Brimlo Software – Business Card Set</title>
<link href="https://fonts.googleapis.com/css2?family=Source+Sans+3:wght@400;600;700&display=swap" rel="stylesheet">
<style>
  :root {
    --backdrop: #b48d63;
    --card-white: #ffffff;
    --ink-dark: #323132;
    --brand-blue: #4a72b8;
    --text-grey: #3c3c3c;
    --label-ink: #1f1a14;
    --card-black: #050505;
    --slate-top: #2f3036;
    --slate-bottom: #4a5a80;
    --font-main: "Source Sans 3", "Myriad Pro", Arial, sans-serif;
  }
  * { margin: 0; padding: 0; box-sizing: border-box; }
  html, body { width: 1200px; height: 788px; overflow: hidden; }
  body { background: var(--backdrop); font-family: var(--font-main); position: relative; }

  .side-label {
    position: absolute; width: 526px; text-align: center;
    font-size: 21px; color: var(--label-ink);
  }
  .card {
    position: absolute; width: 526px; height: 300px; border-radius: 22px;
    overflow: hidden; box-shadow: 0 4px 10px rgba(0,0,0,0.35);
  }
  .card--front { left: 56px; top: 74px; background: var(--card-white); }
  .card--back-light { left: 622px; top: 74px; background: var(--card-white); }
  .card--back-black { left: 53px; top: 446px; background: var(--card-black); }
  .card--back-slate { left: 622px; top: 446px;
    background: radial-gradient(ellipse 90% 80% at 50% 100%, var(--slate-bottom), var(--slate-top)); }

  .brand { position: absolute; display: flex; align-items: center; }
  .brand__dot { border-radius: 50%; background: var(--brand-blue); flex: none; }
  .brand__name { font-weight: 600; color: var(--ink-dark); line-height: 1; letter-spacing: 1px; }
  .brand--small { left: 70px; top: 88px; gap: 18px; }
  .brand--small .brand__dot { width: 74px; height: 74px; }
  .brand--small .brand__name { font-size: 64px; }
  .brand--large { left: 0; right: 0; justify-content: center; top: 90px; gap: 26px; }
  .brand--large .brand__dot { width: 104px; height: 104px; }
  .brand--large .brand__name { font-size: 92px; }
  .brand--white .brand__name { color: #fff; }

  .website {
    position: absolute; left: 0; right: 0; text-align: center;
    font-size: 19px; letter-spacing: 4.5px; color: var(--text-grey); top: 248px;
  }
  .website--light { color: #fff; top: 254px; }

  .person { position: absolute; left: 70px; top: 222px; }
  .person__name { font-size: 18.5px; font-weight: 700; color: var(--brand-blue); }
  .person__role { font-size: 13px; color: var(--text-grey); margin-top: 1px; }

  .contact { position: absolute; left: 326px; top: 227px; font-size: 14px; color: var(--text-grey); }
  .contact__row { display: flex; align-items: center; gap: 8px; height: 19px; }
  .contact__row svg { width: 9px; height: 9px; fill: var(--text-grey); }

  .texture { position: absolute; inset: 0; }
  .card--back-black .brand, .card--back-black .website { z-index: 1; }
</style>
</head>
<body>
  <div class="side-label" style="left:56px; top:34px;">Front</div>
  <div class="side-label" style="left:622px; top:34px;">Back - 1</div>
  <div class="side-label" style="left:53px; top:404px;">Back - 2</div>
  <div class="side-label" style="left:622px; top:404px;">Back - 3</div>

  <section class="card card--front">
    <div class="brand brand--small">
      <span class="brand__dot"></span>
      <span class="brand__name">brimlo</span>
    </div>
    <div class="person">
      <div class="person__name">First Name Last Name</div>
      <div class="person__role">Designation</div>
    </div>
    <div class="contact">
      <div class="contact__row">
        <svg viewBox="0 0 10 10"><path d="M2 0.5 L3.8 2.6 L2.8 3.8 Q4 6.2 6.2 7.2 L7.4 6.2 L9.5 8 L8.2 9.5 Q3.5 9 0.5 1.8 Z"/></svg>
        <span>+12 345 6789</span>
      </div>
      <div class="contact__row">
        <svg viewBox="0 0 10 10"><path d="M0.5 2.5 H9.5 V8.5 H0.5 Z M1 3 L5 6 L9 3" stroke="#fff" stroke-width="0.8"/></svg>
        <span>info@website.com</span>
      </div>
    </div>
  </section>

  <section class="card card--back-light">
    <div class="brand brand--large">
      <span class="brand__dot"></span>
      <span class="brand__name">brimlo</span>
    </div>
    <div class="website">www.website.com</div>
  </section>

  <section class="card card--back-black">
    <svg class="texture" viewBox="0 0 526 300" role="img" aria-label="Perforated metal dot texture glowing in the top-left and bottom-right corners">
      <defs>
        <radialGradient id="glow-top" cx="0.3" cy="0" r="0.5">
          <stop offset="0" stop-color="#6b6b6b" stop-opacity="0.7"/>
          <stop offset="1" stop-color="#000" stop-opacity="0"/>
        </radialGradient>
        <radialGradient id="glow-bottom" cx="0.78" cy="0.85" r="0.45">
          <stop offset="0" stop-color="#7a7070" stop-opacity="0.7"/>
          <stop offset="1" stop-color="#000" stop-opacity="0"/>
        </radialGradient>
      </defs>
      <rect width="526" height="300" fill="url(#glow-top)"/>
      <rect width="526" height="300" fill="url(#glow-bottom)"/>
    </svg>
    <div class="brand brand--large brand--white">
      <span class="brand__dot"></span>
      <span class="brand__name">brimlo</span>
    </div>
    <div class="website website--light">www.website.com</div>
  </section>

  <section class="card card--back-slate">
    <div class="brand brand--large brand--white">
      <span class="brand__dot"></span>
      <span class="brand__name">brimlo</span>
    </div>
    <div class="website website--light">www.website.com</div>
  </section>
</body>
</html>
```